Business card design Needed for new logo / Construction business, home extensions and new builds

We need a business card design using our new logo files which i will attach to this project :)

We are a small construction business specialising in home extensions, new builds and property development. We are very ambitious and would appreciate professional and elegant designs for our new business card.

Very serious about using the services on BriefNest and recently acquired our new logo from here :)

Please get involved, i will feedback when i can as i am very busy but can respond daily, thanks

Target Market(s)

People that want to build onto their houses, new building developments or adding too their existing property

Industry/Entity Type

Construction

Contact Information for Business Card

Hollin Marsh Construction, Tobias Renwick (Managing Director), Tel 07822200444, email - info@hollin-marsh, www.hollin-marsh.co.uk

Colors

Designer to choose colors to be used in the design.

Requirements
Must have
• I like a deep grey on the back please. A lot of you have provided black from and back, try mixing things up a little. The black looks cool 😎 Thanks

```html
<!DOCTYPE html>
<html lang="en">
<head>
<meta charset="utf-8">
<title>Hollin Marsh Construction — Business Card</title>
<link href="https://fonts.googleapis.com/css2?family=Cinzel:wght@400;500;600&display=swap" rel="stylesheet">
<style>
  :root {
    --page: #e6e6e6;
    --card-grey: #2b2b2e;
    --card-grey-light: #38383c;
    --card-black: #050505;
    --card-white: #ffffff;
    --gold: #d9a233;
    --silver: #d2d2d5;
    --ink: #2a2a2a;
    --pattern-light: #fbf7ee;
  }
  * { box-sizing: border-box; margin: 0; padding: 0; }
  html, body {
    width: 846px; height: 1200px; overflow: hidden;
    background: var(--page);
    font-family: "Cinzel", serif;
  }
  .sheet {
    width: 846px; height: 1200px;
    display: flex; flex-direction: column;
    align-items: center; justify-content: center;
    gap: 60px;
  }
  .card {
    position: relative;
    width: 680px; height: 406px;
    border-radius: 34px;
    overflow: hidden;
    box-shadow: 0 10px 26px rgba(0,0,0,0.22);
  }

  /* Back of card */
  .card--back { background: var(--card-grey); }
  .card__pattern {
    position: absolute; inset: 0;
    background: radial-gradient(circle at 50% 45%, var(--card-grey-light), var(--card-grey) 75%);
  }
  .brand {
    position: absolute; inset: 0;
    display: flex; flex-direction: column;
    align-items: center; justify-content: center;
    gap: 18px;
    color: var(--silver);
    font-weight: 500;
  }
  .brand__dot {
    width: 20px; height: 20px; border-radius: 50%;
    background: var(--gold);
  }
  .brand__name {
    text-align: center;
    font-size: 30px;
    letter-spacing: 1.5px;
    line-height: 1.2;
    text-transform: uppercase;
  }
  .brand__name span { display: block; font-size: 21px; letter-spacing: 3px; }

  /* Front of card */
  .card--front { background: var(--card-white); }
  .card__pattern--light {
    background: linear-gradient(135deg, var(--card-white), var(--pattern-light));
  }
  .card__chevron {
    position: absolute; inset: 0; width: 100%; height: 100%;
  }
  .contact {
    position: absolute; left: 315px; top: 54px;
  }
  .contact__name {
    font-size: 28px; font-weight: 500;
    color: var(--gold);
    letter-spacing: 0.5px;
    text-transform: uppercase;
    line-height: 1.15;
  }
  .contact__role {
    font-size: 18px; color: var(--ink);
    margin-top: 0;
  }
  .contact__list {
    list-style: none;
    margin-top: 66px;
  }
  .contact__item {
    display: flex; align-items: center;
    gap: 12px;
    height: 24px;
    margin-bottom: 20px;
    font-size: 16px; color: var(--ink);
    letter-spacing: 0.4px;
    white-space: nowrap;
  }
  .contact__item--lower { text-transform: none; }
  .contact__icon { width: 25px; height: 25px; flex: none; }
</style>
</head>
<body>
<main class="sheet">

  <section class="card card--back" aria-label="Business card back">
    <div class="card__pattern" role="img" aria-label="Subtle repeating brand pattern on deep grey"></div>
    <div class="brand">
      <div class="brand__dot"></div>
      <p class="brand__name">Hollin Marsh<span>Construction</span></p>
    </div>
  </section>

  <section class="card card--front" aria-label="Business card front">
    <div class="card__pattern card__pattern--light" role="img" aria-label="Faint repeating brand pattern on white" style="position:absolute;inset:0"></div>

    <svg class="card__chevron" viewBox="0 0 745 445" preserveAspectRatio="none" aria-hidden="true">
      <defs>
        <linearGradient id="goldBar" x1="0" y1="0" x2="1" y2="1">
          <stop offset="0" stop-color="#b97f1f"/>
          <stop offset="0.45" stop-color="#f3cf6a"/>
          <stop offset="0.75" stop-color="#d9a233"/>
          <stop offset="1" stop-color="#a8701a"/>
        </linearGradient>
        <linearGradient id="silverBar" x1="0" y1="0" x2="1" y2="1">
          <stop offset="0" stop-color="#8f9095"/>
          <stop offset="0.5" stop-color="#eeeeef"/>
          <stop offset="1" stop-color="#a4a5aa"/>
        </linearGradient>
      </defs>
      <polygon points="0,0 145,0 280,222 145,445 0,445" fill="url(#silverBar)"/>
      <polygon points="0,0 133,0 268,222 133,445 0,445" fill="#050505"/>
      <polygon points="126,22 170,22 263,180 219,180" fill="url(#goldBar)"/>
      <polygon points="160,22 178,22 271,180 253,180" fill="url(#silverBar)"/>
      <polygon points="213,280 258,280 191,385 148,385" fill="url(#goldBar)"/>
    </svg>

    <div class="contact">
      <h1 class="contact__name">Tobias Renwick</h1>
      <p class="contact__role">Managing Director</p>
      <ul class="contact__list">
        <li class="contact__item">
          <svg class="contact__icon" viewBox="0 0 24 24" aria-hidden="true"><circle cx="12" cy="12" r="12" fill="#d9a233"/><path d="M12 5.5a4 4 0 0 0-4 4c0 3 4 8 4 8s4-5 4-8a4 4 0 0 0-4-4z" fill="#fff"/><circle cx="12" cy="9.5" r="1.5" fill="#d9a233"/></svg>
          14 Kestrel Row, Leeds
        </li>
        <li class="contact__item">
          <svg class="contact__icon" viewBox="0 0 24 24" aria-hidden="true"><circle cx="12" cy="12" r="12" fill="#d9a233"/><rect x="6" y="8" width="12" height="8.5" rx="1" fill="#fff"/><path d="M6.5 8.5 12 13l5.5-4.5" fill="none" stroke="#d9a233" stroke-width="1"/></svg>
          info@hollin-marsh
        </li>
        <li class="contact__item">
          <svg class="contact__icon" viewBox="0 0 24 24" aria-hidden="true"><circle cx="12" cy="12" r="12" fill="#d9a233"/><g fill="none" stroke="#fff" stroke-width="1.1"><circle cx="12" cy="12" r="6"/><ellipse cx="12" cy="12" rx="2.6" ry="6"/><path d="M6 12h12M7 9h10M7 15h10"/></g></svg>
          www.hollin-marsh.co.uk
        </li>
        <li class="contact__item">
          <svg class="contact__icon" viewBox="0 0 24 24" aria-hidden="true"><circle cx="12" cy="12" r="12" fill="#d9a233"/><path d="M8.5 6.5l2 2.2-1.2 1.6a7 7 0 0 0 4.4 4.4l1.6-1.2 2.2 2-1.3 1.8c-4.6-.2-9-4.6-9.2-9.2z" fill="#fff"/></svg>
          07822200444
        </li>
      </ul>
    </div>
  </section>

</main>
</body>
</html>
```